Stationary for new financial planning firm
Meadowlark Financial Planning
Stationary for new financial planning firm - Financial Services
Creative Brief
Professional
Doran Velsik
Principal
218 West K Ave, Suite 307 Petaluma, CA 94958
doran@meadowlarkfp.example
www.MeadowlarkFinancialPlanning.example or meadowlarkfp.example (either one works)
Meadowlark Financial Planning is a values-based financial planning and investment advisory firm dedicated to the creation, implementation and management of sound financial strategies that allow clients to achieve their financial goals. Our mission is to deliver three things: time, wisdom and trust. By helping you create more time in your life, being your primary source of financial wisdom, and building long-term trust, we aim to be your advisor for life.
QZMtlb QZMtlb
I would like this printed on the back side. I know it is a lot of text, but it is included on my current cards and is fine. "Meadowlark Financial Planning is a values-based financial planning and investment advisory firm dedicated to the creation, implementation and management of sound financial strategies that allow clients to achieve their financial goals. Our mission is to deliver three things: time, wisdom and trust. By helping you create more time in your life, being your primary source of financial wisdom, and building long-term trust, we aim to be your advisor for life."

```html
<!DOCTYPE html>
<html lang="en">
<head>
<meta charset="utf-8">
<title>Meadowlark Financial Planning – Business Cards</title>
<link href="https://fonts.googleapis.com/css2?family=Cinzel:wght@400&family=Lato:wght@400;700&display=swap" rel="stylesheet">
<style>
  :root {
    --bg: #8d8d8d;
    --green: #6aa843;
    --green-dark: #55902f;
    --green-light: #8cc063;
    --brown: #7a5430;
    --white: #ffffff;
    --ink-green: #5e9a38;
  }
  html, body {
    margin: 0;
    padding: 0;
    overflow: hidden;
  }
  .canvas {
    width: 1200px;
    height: 908px;
    background: radial-gradient(ellipse at 50% 40%, #a2a2a2 0%, var(--bg) 70%, #767676 100%);
    position: relative;
    overflow: hidden;
  }
  .card {
    position: absolute;
    top: 300px;
    width: 540px;
    height: 309px;
    border-radius: 22px;
    overflow: hidden;
    box-shadow: 0 10px 24px rgba(0,0,0,.28);
  }
  .card--front {
    left: 40px;
    background: linear-gradient(135deg, var(--green-light) 0%, var(--green) 45%, var(--green-dark) 100%);
  }
  .card--back {
    left: 620px;
    background: var(--white);
  }
  .tree-art {
    position: absolute;
    left: 250px;
    top: 10px;
    width: 220px;
    height: 160px;
    border-radius: 50%;
    background: radial-gradient(ellipse at 50% 45%, rgba(255,255,255,.28) 0%, rgba(255,255,255,.12) 55%, rgba(255,255,255,0) 75%);
  }
  .brand {
    font-family: "Cinzel", serif;
    font-weight: 400;
    letter-spacing: 2px;
    line-height: 1.15;
    text-transform: uppercase;
    margin: 0;
  }
  .card--front .brand {
    position: absolute;
    left: 0;
    right: 0;
    top: 150px;
    text-align: center;
    color: var(--white);
    font-size: 24px;
  }
  .mission {
    position: absolute;
    left: 34px;
    right: 34px;
    bottom: 20px;
    margin: 0;
    font-family: "Lato", sans-serif;
    font-size: 9px;
    line-height: 1.45;
    color: var(--white);
    text-align: center;
  }
  .brand-lockup {
    position: absolute;
    left: 150px;
    top: 40px;
    display: flex;
    align-items: center;
    gap: 12px;
  }
  .brand-mark {
    width: 34px;
    height: 34px;
    background: var(--ink-green);
  }
  .card--back .brand {
    color: var(--ink-green);
    font-size: 20px;
  }
  .wave {
    position: absolute;
    inset: 0;
    width: 100%;
    height: 100%;
  }
  .contact {
    position: absolute;
    left: 26px;
    bottom: 14px;
    margin: 0;
    padding: 0;
    list-style: none;
    font-family: "Lato", sans-serif;
    font-size: 10px;
    line-height: 1.5;
    color: var(--white);
  }
  .contact li {
    display: flex;
    align-items: center;
    gap: 6px;
  }
  .contact svg {
    width: 10px;
    height: 10px;
    flex: none;
  }
  .person {
    position: absolute;
    right: 28px;
    bottom: 30px;
    text-align: right;
    font-family: "Lato", sans-serif;
    color: var(--white);
  }
  .person__name {
    font-size: 20px;
    font-weight: 700;
    margin: 0;
  }
  .person__title {
    font-size: 13px;
    margin: 2px 0 0;
  }
</style>
</head>
<body>
<div class="canvas">

  <section class="card card--front">
    <div class="tree-art" role="img" aria-label="Tree illustration with a figure reaching upward"></div>
    <p class="brand">Meadowlark<br>Financial Planning</p>
    <p class="mission">Meadowlark Financial Planning is a values-based financial planning and investment advisory firm dedicated to the creation, implementation and management of sound financial strategies that allow clients to achieve their financial goals. Our mission is to deliver three things: time, wisdom and trust. By helping you create more time in your life, being your primary source of financial wisdom, and building long-term trust, we aim to be your advisor for life.</p>
  </section>

  <section class="card card--back">
    <div class="brand-lockup">
      <div class="brand-mark"></div>
      <p class="brand">Meadowlark<br>Financial Planning</p>
    </div>

    <svg class="wave" viewBox="0 0 540 309" preserveAspectRatio="none" aria-hidden="true">
      <path d="M0 170 C150 150 300 190 540 80 L540 92 C300 204 150 164 0 182 Z" fill="var(--green-light)"/>
      <path d="M0 186 C150 166 310 206 540 100 L540 118 C310 224 150 184 0 204 Z" fill="var(--brown)"/>
      <path d="M0 210 C150 190 320 230 540 126 L540 309 L0 309 Z" fill="var(--green)"/>
    </svg>

    <ul class="contact">
      <li><svg viewBox="0 0 10 10"><path d="M5 0.5a3.2 3.2 0 0 0-3.2 3.2C1.8 6.2 5 9.5 5 9.5s3.2-3.3 3.2-5.8A3.2 3.2 0 0 0 5 0.5z" fill="#fff"/><circle cx="5" cy="3.7" r="1.2" fill="var(--green)"/></svg>218 West K Ave, Suite 307 Petaluma, CA 94958</li>
      <li><svg viewBox="0 0 10 10"><circle cx="5" cy="5" r="5" fill="#fff"/><path d="M3.2 2.5l1 1-.6.8c.4.8 1 1.4 1.8 1.8l.8-.6 1 1-.7.9C4.8 7.3 2.7 5.2 2.5 3.4z" fill="var(--green)"/></svg>707.555.0148</li>
      <li><svg viewBox="0 0 10 10"><circle cx="5" cy="5" r="5" fill="#fff"/><rect x="2.8" y="3" width="4.4" height="4" fill="var(--green)"/></svg>707.555.0149</li>
      <li><svg viewBox="0 0 10 10"><circle cx="5" cy="5" r="5" fill="#fff"/><rect x="2.5" y="3.2" width="5" height="3.6" fill="none" stroke="var(--green)" stroke-width=".8"/><path d="M2.5 3.2L5 5.2 7.5 3.2" fill="none" stroke="var(--green)" stroke-width=".8"/></svg>doran@meadowlarkfp.example</li>
      <li><svg viewBox="0 0 10 10"><circle cx="5" cy="5" r="5" fill="#fff"/><circle cx="5" cy="5" r="2.6" fill="none" stroke="var(--green)" stroke-width=".8"/><path d="M2.4 5h5.2" stroke="var(--green)" stroke-width=".8"/></svg>www.meadowlarkfp.example</li>
    </ul>

    <div class="person">
      <p class="person__name">Doran Velsik</p>
      <p class="person__title">Principal</p>
    </div>
  </section>

</div>
</body>
</html>
```